Junge Steuerberaterin sucht ansprechendes Design für Logo und Geschäftsausstattung
Zielgruppe
Steuerberatung für jegliche Zielgruppe
Aufgabenstellung
Das Design sollte frisch und modern sein und dennoch seriös.
Ich könnte mir von den Farben her grün und orange gut vorstellen oder aber rot (ggf. auch mit zweiter Farbe). Grundsätzlich bin ich aber für jede Farbe(-Kombi) offen.
Die Initialen LM sollten NICHT hervorgehoben werden.

```html
<!DOCTYPE html>
<html lang="de">
<head>
<meta charset="utf-8">
<title>Luna Mor Steuerberatung – Geschäftsausstattung</title>
<link href="https://fonts.googleapis.com/css2?family=Quicksand:wght@400;500&family=Open+Sans:wght@400;700&display=swap" rel="stylesheet">
<style>
  :root {
    --green: #7aab2a;
    --green-light: #9cc63b;
    --orange: #ee7d12;
    --orange-deep: #e8650f;
    --yellow: #f9c012;
    --grey-text: #8a8a8a;
    --ink: #333;
    --paper: #f4f4f4;
    --stage: #e6e7e8;
    --white: #fff;
  }
  * { margin: 0; padding: 0; box-sizing: border-box; }
  html, body { width: 743px; height: 1200px; overflow: hidden; }
  body { position: relative; background: var(--white); font-family: "Open Sans", sans-serif; }

  .brand-name { font-family: "Quicksand", sans-serif; font-weight: 400; color: var(--orange); letter-spacing: 0.02em; white-space: nowrap; }
  .brand-tag { font-family: "Quicksand", sans-serif; color: var(--grey-text); letter-spacing: 0.32em; text-transform: uppercase; white-space: nowrap; }

  /* Logo section */
  .logo-section { position: absolute; left: 0; top: 0; width: 743px; height: 200px; background: var(--white); }
  .logo-section .brand { position: absolute; left: 0; right: 0; top: 64px; text-align: center; }
  .logo-section .brand-name { font-size: 42px; line-height: 1; }
  .logo-section .brand-tag { font-size: 8px; margin-top: 6px; }

  /* Card section */
  .cards-section { position: absolute; left: 0; top: 200px; width: 743px; height: 488px; background: var(--stage); }
  .card { position: absolute; top: 141px; width: 340px; height: 206px; overflow: hidden; background: var(--white); box-shadow: 0 3px 10px rgba(0,0,0,.18); }
  .card-front { left: 21px; background: linear-gradient(135deg, var(--orange-deep) 0%, var(--orange) 45%, var(--yellow) 100%); }
  .card-front .white-panel { position: absolute; right: 0; top: 72px; width: 150px; height: 104px; background: var(--white); }
  .card-front .white-corner { position: absolute; left: 0; bottom: 0; width: 70px; height: 30px; background: var(--white); }
  .card-front .holder-name { position: absolute; left: 20px; top: 18px; font-family: "Quicksand", sans-serif; font-size: 26px; color: var(--white); }
  .card-front .holder-role { position: absolute; left: 20px; top: 50px; font-family: "Quicksand", sans-serif; font-size: 12px; color: var(--green-light); }
  .card-front .divider { position: absolute; left: 20px; top: 68px; width: 150px; height: 1px; background: var(--green-light); }
  .card-front .address { position: absolute; left: 20px; top: 82px; font-family: "Quicksand", sans-serif; font-size: 11px; line-height: 1.35; color: var(--white); }
  .card-front .address .web { color: var(--green-light); font-weight: 500; }
  .card-front .panel-brand { position: absolute; right: 0; top: 100px; width: 150px; text-align: center; }
  .card-front .panel-brand .brand-name { font-size: 22px; }
  .card-front .panel-brand .brand-tag { font-size: 5px; margin-top: 3px; }
  .card-front .contact { position: absolute; left: 90px; bottom: 5px; font-family: "Quicksand", sans-serif; font-size: 10px; line-height: 1.3; color: var(--white); white-space: nowrap; }

  .card-back { left: 382px; }
  .card-back .green-square { position: absolute; left: 18px; top: 0; width: 60px; height: 46px; background: linear-gradient(135deg, var(--green), var(--green-light)); }
  .card-back .back-brand { position: absolute; left: 0; right: 0; top: 70px; text-align: center; }
  .card-back .back-brand .brand-name { font-size: 30px; }
  .card-back .back-brand .brand-tag { font-size: 6px; margin-top: 4px; }
  .card-back .web-band { position: absolute; right: 0; bottom: 24px; width: 170px; height: 30px; background: linear-gradient(90deg, var(--orange), var(--orange-deep)); font-family: "Quicksand", sans-serif; font-size: 11px; letter-spacing: 0.2em; color: var(--green-light); line-height: 30px; padding-left: 14px; white-space: nowrap; }

  /* Letter section */
  .letter-section { position: absolute; left: 0; top: 688px; width: 743px; height: 512px; background: linear-gradient(135deg, #c9cbcd, var(--stage) 60%, #d8d9da); }
  .letter { position: absolute; left: 238px; top: 101px; width: 261px; height: 373px; background: var(--paper); box-shadow: 0 6px 16px rgba(0,0,0,.25); font-size: 4.6px; color: var(--ink); }
  .letter .head-green { position: absolute; left: 0; top: 10px; width: 38px; height: 26px; background: var(--green); }
  .letter .head-orange { position: absolute; right: 0; top: 10px; width: 133px; height: 26px; background: var(--orange); }
  .letter .head-brand { position: absolute; left: 42px; top: 12px; width: 82px; text-align: center; }
  .letter .head-brand .brand-name { font-size: 13px; line-height: 1.1; }
  .letter .head-brand .brand-tag { font-size: 3px; letter-spacing: 0.25em; }
  .letter .recipient { position: absolute; left: 40px; top: 62px; line-height: 1.35; color: #555; }
  .letter .sender { position: absolute; left: 175px; top: 62px; line-height: 1.35; color: #555; }
  .letter .sender p + p { margin-top: 5px; }
  .letter .subject { position: absolute; left: 40px; top: 120px; font-weight: 700; font-size: 4.8px; }
  .letter .body { position: absolute; left: 40px; top: 137px; width: 190px; line-height: 2; color: #444; }
  .letter .body p { margin-bottom: 6px; }
  .letter .signature { position: absolute; left: 39px; top: 294px; width: 44px; height: 10px; background: var(--orange); opacity: .35; }
  .letter .foot-green { position: absolute; left: 0; bottom: 0; width: 100px; height: 25px; background: var(--green); }
  .letter .foot-orange { position: absolute; right: 0; bottom: 0; width: 161px; height: 25px; background: #d97f12; }
</style>
</head>
<body>

<section class="logo-section">
  <div class="brand">
    <div class="brand-name">Luna Mor</div>
    <div class="brand-tag">Steuerberatung</div>
  </div>
</section>

<section class="cards-section">
  <div class="card card-front">
    <div class="white-panel"></div>
    <div class="white-corner"></div>
    <div class="holder-name">Luna Mor</div>
    <div class="holder-role">Steuerberaterin</div>
    <div class="divider"></div>
    <div class="address">
      <div class="web">Luna-Mor.de</div>
      <div>Lindenweg 42</div>
      <div>4512X Beispielstadt</div>
    </div>
    <div class="panel-brand">
      <div class="brand-name">Luna Mor</div>
      <div class="brand-tag">Steuerberatung</div>
    </div>
    <div class="contact">
      <div>Mail.: kontakt@luna-mor.de</div>
      <div>Tel. : 0160 / 38 XX 217</div>
    </div>
  </div>

  <div class="card card-back">
    <div class="green-square"></div>
    <div class="back-brand">
      <div class="brand-name">Luna Mor</div>
      <div class="brand-tag">Steuerberatung</div>
    </div>
    <div class="web-band">www.luna-mor.de</div>
  </div>
</section>

<section class="letter-section">
  <article class="letter">
    <div class="head-green"></div>
    <div class="head-brand">
      <div class="brand-name">Luna Mor</div>
      <div class="brand-tag">Steuerberatung</div>
    </div>
    <div class="head-orange"></div>

    <div class="recipient">
      <p>Herr Beispiel<br>Ahornallee 77<br>4512X Beispielstadt</p>
    </div>
    <div class="sender">
      <p>Frau Luna Mor<br>Morweg 56<br>51233 Beispielstadt</p>
      <p>Tel.: 3671 / 48XX902<br>Mail: info@mor.de<br>Web: luna-mor.de</p>
    </div>

    <div class="subject">Steuererklärung für das Jahr 2014</div>

    <div class="body">
      <p>Lorem ipsum dolor sit amet, consetetur sadipscing elitr, sed diam nonumy eirmod tempor invidunt ut labore et dolore magna aliquyam erat, sed diam voluptua. At vero eos et accusam et justo duo dolores et ea rebum. Stet clita kasd gubergren, no sea takimata sanctus est Lorem ipsum dolor sit amet.</p>
      <p>dolores et ea rebum. Stet clita kasd gubergren, no sea takimata sanctus est Lorem ipsum dolor sit amet. Lorem ipsum dolor sit amet, consetetur sadipscing elitr, sed diam nonumy eirmod tempor invidunt ut labore et dolore magna aliquyam erat, sed diam.</p>
      <p>Duis autem vel eum iriure dolor in hendrerit in vulputate velit esse molestie consequat, vel illum dolore eu feugiat nulla facilisis at vero eros et accumsan et iusto odio dignissim qui blandit praesent luptatum zzril delenit augue duis dolore te feugait nulla facilisi. Lorem ipsum dolor sit amet, consectetuer adipiscing elit, sed diam nonummy nibh euismod tincidunt ut laoreet dolore magna aliquam erat volutpat.</p>
      <p>Mit freundlichen Grüßen</p>
    </div>
    <div class="signature" role="img" aria-label="Handschriftliche Unterschrift"></div>

    <div class="foot-green"></div>
    <div class="foot-orange"></div>
  </article>
</section>

</body>
</html>
```